Business Card For Video Production Company

Please NOTE: I've added some info to the must haves that I should have included at the start. Thank you.

I need a business card design for my video production company based in Orlando called Caldera Film Works. Our work consists of web video marketing (web videos), training videos, sales videos, conference and seminar video production...basically a lot of corporate based work.

We work with successful small businesses, not-for-profits and some Fortune 500 type groups. We bring a lot of knowledge, experience and attention to detail to every project.

I'd like something that communicates strength, confidence, integrity, as well as creative vision. I want to stay away from the standard icons of the media and film industry. I'd like to emphasize the colors of my logo, and also the colors of my website which has a white background. Simple is good.

Our budgets are moderate...generally $1500 to $5000.

www.calderafilm.tv

PS...We don't do weddings or recitals, or that type of production.
Updates

I want to thank all the designers for your updates. There's way too many to be able to give feedback on for all. I hope you understand that. But wow…there are so many great designs everyone has offered. I can't thank you enough…each and everyone. I hope to make my decision soon. I'm not accepting anymore designs from new designers. Brent-

Target Market(s)

Successful small businesses, marketing directors, corporate communication directors, training and human resources professionals. forward thinking not-for profits. Since my company is based in Central Florida, most of my work comes from this area too.

Industry/Entity Type

Marketing

Requirements
Must have
• website address, www.calderafilm.tv
phone number, 407-552-9031
email address, brent@calderafilm.tv

Title
Brent Caldera
Owner/Creative Director

I'd like to have a single line that goes across illustrating our services, maybe separated with bullet points:

Marketing Videos, Corporate Videos, Conference & Seminar Video Production
Should not have
• No film or video icons.
No need to pull language or copy from my website.

```html
<!DOCTYPE html>
<html lang="en">
<head>
<meta charset="utf-8">
<title>Caldera Film Works — Business Card</title>
<link rel="stylesheet" href="https://fonts.googleapis.com/css2?family=Montserrat:wght@700&family=Open+Sans:wght@400;600&display=swap">
<style>
  :root {
    --brand-blue: #2a90d6;
    --ink-dark: #3a3d42;
    --ink-body: #4a4d52;
    --card-white: #ffffff;
    --page-bg: #e9eaec;
    --divider: #cfd3d8;
  }
  * { box-sizing: border-box; margin: 0; padding: 0; }
  html, body { width: 1200px; height: 829px; overflow: hidden; }
  body {
    background: var(--page-bg);
    font-family: "Open Sans", Arial, sans-serif;
    position: relative;
  }
  .card {
    position: absolute;
    width: 520px;
    height: 297px;
    border-radius: 4px;
    box-shadow: 0 6px 18px rgba(0,0,0,0.15);
    overflow: hidden;
  }
  /* Front: contact side */
  .card-front {
    left: 50px;
    top: 266px;
    background: var(--card-white);
    display: flex;
  }
  .side-band {
    width: 70px;
    background: var(--brand-blue);
    border-right: 6px solid var(--divider);
    flex-shrink: 0;
  }
  .front-content {
    padding: 34px 0 0 34px;
  }
  .brand {
    display: flex;
    align-items: center;
    gap: 12px;
  }
  .brand-square {
    width: 34px;
    height: 34px;
    background: var(--brand-blue);
  }
  .brand-name {
    font-family: "Montserrat", Arial, sans-serif;
    font-weight: 700;
    font-size: 26px;
    color: var(--ink-dark);
    letter-spacing: -0.3px;
  }
  .person { margin-top: 42px; }
  .person-name {
    font-weight: 600;
    font-size: 19px;
    color: var(--brand-blue);
  }
  .person-title {
    font-size: 13px;
    color: var(--ink-body);
    margin-top: 2px;
  }
  .contact {
    list-style: none;
    margin-top: 18px;
    font-size: 13px;
    color: var(--ink-body);
    line-height: 1.75;
  }
  /* Back: brand side */
  .card-back {
    left: 630px;
    top: 266px;
    background: var(--brand-blue);
    color: var(--card-white);
    display: flex;
    flex-direction: column;
    align-items: center;
    padding-top: 72px;
  }
  .back-name {
    font-family: "Montserrat", Arial, sans-serif;
    font-weight: 700;
    font-size: 40px;
    letter-spacing: -0.5px;
  }
  .services {
    list-style: none;
    margin-top: 44px;
    font-size: 15px;
    text-align: center;
    line-height: 1.8;
  }
  .services li { display: inline-flex; align-items: center; gap: 7px; margin: 0 7px; }
  .bullet {
    width: 9px;
    height: 9px;
    background: var(--card-white);
    opacity: 0.85;
  }
</style>
</head>
<body>
  <section class="card card-front" aria-label="Business card front">
    <div class="side-band"></div>
    <div class="front-content">
      <div class="brand">
        <span class="brand-square"></span>
        <span class="brand-name">Caldera Film Works</span>
      </div>
      <div class="person">
        <p class="person-name">Brent Caldera</p>
        <p class="person-title">Owner/Creative Director</p>
      </div>
      <ul class="contact">
        <li>407-552-9031</li>
        <li>brent@calderafilm.tv</li>
        <li>www.calderafilm.tv</li>
      </ul>
    </div>
  </section>

  <section class="card card-back" aria-label="Business card back">
    <h1 class="back-name">Caldera Film Works</h1>
    <ul class="services">
      <li><span class="bullet"></span>Marketing Videos</li>
      <li><span class="bullet"></span>Corporate Videos</li>
      <li><span class="bullet"></span>Conference &amp; Seminar Video Production</li>
    </ul>
  </section>
</body>
</html>
```